Kentucky residential recovery center needs a flyer design

We need a flyer design for a 16 bed male residential/inpatient recovery center based in Richmond, Kentucky. The facility provides short term (average 30 day) treatment to those struggling with substace abuse and addiction. The design should communicate trust, assurance, safety.
Our wesite provides more information https://morvalcare.org/treatment-services/residential-treatment/

Target Market(s)

Men (typically 30-50) struggling with substance addiction

```html
<!DOCTYPE html>
<html lang="en">
<head>
<meta charset="utf-8">
<title>Morval Care – Residential Recovery Flyer</title>
<link rel="stylesheet" href="https://fonts.googleapis.com/css2?family=Montserrat:ital,wght@0,500;0,600;0,700;0,800;1,700&display=swap">
<style>
  :root {
    --navy: #1b2a4e;
    --ink: #1b2a4e;
    --muted: #b7bfd2;
    --paper: #ffffff;
    --photo-sky: #8fb6e6;
    --photo-brick: #8b5a44;
    --room-warm: #6f5a4a;
  }
  * { box-sizing: border-box; margin: 0; padding: 0; }
  html, body { width: 848px; height: 1200px; overflow: hidden; background: var(--paper); }
  body { font-family: "Montserrat", sans-serif; color: var(--ink); }
  .flyer { position: relative; width: 848px; height: 1200px; background: var(--paper); overflow: hidden; }

  .brand { position: absolute; left: 58px; top: 40px; display: flex; align-items: center; gap: 10px; }
  .brand-dot { width: 22px; height: 22px; border-radius: 50%; background: var(--navy); }
  .brand-name { font-weight: 800; font-size: 17px; letter-spacing: 1.5px; color: var(--navy); text-transform: uppercase; }

  .hero-photo {
    position: absolute; left: 0; top: 178px; width: 539px; height: 590px;
    background: linear-gradient(180deg, var(--photo-sky) 0%, #c9d6e6 30%, #a87a62 62%, var(--photo-brick) 100%);
  }

  .headline-panel {
    position: absolute; left: 425px; top: 66px; width: 406px; height: 439px;
    background: var(--navy); border-radius: 34px;
    padding: 64px 0 0 21px; color: var(--paper);
  }
  .headline { font-weight: 800; font-size: 58px; line-height: 1.03; letter-spacing: -0.5px; text-transform: uppercase; }
  .headline-sub { margin-top: 14px; font-weight: 500; font-size: 31px; line-height: 1.25; color: var(--muted); text-transform: uppercase; letter-spacing: 0.5px; }

  .stat { position: absolute; left: 548px; width: 220px; text-align: center; }
  .stat-value { display: block; font-weight: 800; font-size: 32px; line-height: 1; color: var(--navy); }
  .stat-label { display: block; margin-top: 7px; font-weight: 700; font-size: 11.5px; color: var(--navy); text-transform: uppercase; }
  .stat.years { top: 524px; }
  .stat.rating { top: 601px; }
  .stat.rank { top: 675px; }
  .stat.lives { top: 740px; }

  .gallery { position: absolute; left: 11px; top: 769px; display: flex; gap: 7px; background: var(--paper); padding-top: 0; }
  .gallery-tile { width: 173px; height: 107px; border-radius: 22px 0 0 0; }
  .gallery-tile.meeting { background: linear-gradient(160deg, #e9e6e1, #4a4440); }
  .gallery-tile.lounge { background: linear-gradient(160deg, #d9d2c8, var(--room-warm)); }
  .gallery-tile.bedroom { background: linear-gradient(160deg, #cfc7bd, #3f3935); }

  .feature { position: absolute; top: 912px; width: 290px; text-align: center; white-space: nowrap; }
  .feature.care { left: -10px; }
  .feature.staff { left: 257px; }
  .feature.safety { left: 532px; }
  .feature-dot { width: 30px; height: 30px; margin: 0 auto 18px; border-radius: 50%; background: var(--navy); }
  .feature-title { font-weight: 700; font-size: 13px; color: var(--navy); text-transform: uppercase; line-height: 1.1; }
  .feature-text { font-weight: 600; font-size: 10px; color: var(--navy); text-transform: uppercase; }
  .feature-rule { width: 91px; height: 3px; margin: 22px auto 0; background: var(--navy); }

  .contact-band {
    position: absolute; left: 88px; top: 1083px; width: 760px; height: 117px;
    background: var(--navy); border-radius: 30px 0 0 0; color: var(--paper);
  }
  .contact-phone { position: absolute; left: 54px; top: 26px; font-weight: 700; font-size: 36px; letter-spacing: -0.5px; }
  .contact-web { position: absolute; left: 122px; top: 74px; font-weight: 700; font-style: italic; font-size: 17px; color: var(--muted); }
  .contact-address { position: absolute; left: 479px; top: 28px; font-weight: 600; font-size: 17px; line-height: 1.2; color: var(--muted); }
  .contact-transport { display: block; margin-top: 4px; font-weight: 700; font-style: italic; font-size: 14px; line-height: 1.15; text-transform: uppercase; }
</style>
</head>
<body>
<main class="flyer">
  <header class="brand">
    <span class="brand-dot"></span>
    <span class="brand-name">Morval Care</span>
  </header>

  <div class="hero-photo" role="img" aria-label="Photo of a smiling man holding a certificate of completion outside the center"></div>

  <section class="headline-panel">
    <h1 class="headline">Reconnect<br>Recover &amp;<br>Rebuild</h1>
    <p class="headline-sub">Your life at<br>Morval Care</p>
  </section>

  <div class="stat years"><span class="stat-value">10 YRS</span><span class="stat-label">of clinical excellence</span></div>
  <div class="stat rating"><span class="stat-value">95%</span><span class="stat-label">satisfaction rating</span></div>
  <div class="stat rank"><span class="stat-value">#1</span><span class="stat-label">in drug &amp; alcohol rehab</span></div>
  <div class="stat lives"><span class="stat-value">2500+</span><span class="stat-label">lives transformed</span></div>

  <div class="gallery">
    <div class="gallery-tile meeting" role="img" aria-label="Photo of the group meeting room"></div>
    <div class="gallery-tile lounge" role="img" aria-label="Photo of the resident lounge"></div>
    <div class="gallery-tile bedroom" role="img" aria-label="Photo of a resident bedroom"></div>
  </div>

  <div class="feature care">
    <div class="feature-dot"></div>
    <h2 class="feature-title">Comprehensive Care</h2>
    <p class="feature-text">Alcohol, medication and addiction</p>
    <div class="feature-rule"></div>
  </div>
  <div class="feature staff">
    <div class="feature-dot"></div>
    <h2 class="feature-title">Empathetic Professionals</h2>
    <p class="feature-text">Your journey, our commitment</p>
    <div class="feature-rule"></div>
  </div>
  <div class="feature safety">
    <div class="feature-dot"></div>
    <h2 class="feature-title">Safe, Supportive Environment</h2>
    <p class="feature-text">Your well-being is our priority</p>
    <div class="feature-rule"></div>
  </div>

  <footer class="contact-band">
    <p class="contact-phone">(555)014-8820</p>
    <p class="contact-web">www.morvalcare.org</p>
    <p class="contact-address">408 Larkspur Ln,<br>Cedar Hollow, KY 40999
      <span class="contact-transport">Free transport<br>available</span>
    </p>
  </footer>
</main>
</body>
</html>
```